Orbe Trophy Banner 3 Feet by 8 Feet

It seems like the photos i submitted are bad quality. Feel free to find some of your own with better resolution. I am not super picky on what is uses as I think I've conveyed my concept and most of you understand.
FEEL FREE TO GET CREATIVE AND ADD PICS OF UR OWN IF U WANT
I am going to Brazil for orbe trophy as a Fan of Mexico National Soccer team. I need a super bad ass banner design. I am not picky and I am attaching several images that you are free to play with. Requirements are as follow:
1. The two pictures of the saints would be ideal. Blend them in so they dont look like like square images.
2. On the bottom at smaller scale so it doesnt take much space. the fotelia sign with our fotelia user names. so fotelia logo and next to it. @ravitelbor81 @quorvent907 then the following hashtags: #nublandoyo #tiapasaloscaramelos #guardianesdelmaizdorado #verbena2031
3. If you can add the Ondalira Logo (which is a channel logo) somewhere so it grabs attention from media it would be cool. Not mandatory.
4. Logo of mexican national team (this can take a lot of space)
5. Lastly the main text or content which would take most of the space, 'Vamos México, vamos Selección! Contigo siempre de corazón!
IF YOU ARE ABLE TO USE MOST PICTURES AND MAKE IT LOOK NICE AND THAT IT FLOWS YOULL MAKE MY LIFE.
Updates
i made a small change with main text. I really like the mexican national logo as back ground even if i have to lose out on the crappy pixilated images. LIke I've said before u can find better images online. fotelia logo on bottom is important with first user names @ravitelbor81 @quorvent907 followed by all the hashtags
Sorry guys i screwed up the size is not 8 by 10 but 3 feet by 8 feet! I am sorry, I will add additional prize amount for the troubles! I will add additional $30 dollars

```html
<!DOCTYPE html>
<html lang="es">
<head>
<meta charset="utf-8">
<title>Contigo Siempre – Banner</title>
<link rel="stylesheet" href="https://fonts.googleapis.com/css2?family=Comfortaa:wght@600&family=Open+Sans:wght@400&family=Poppins:wght@600&display=swap">
<style>
  :root {
    --green-deep: #1c4a3a;
    --green-band: #1f6b45;
    --green-mid: #2a7d52;
    --green-text: #1b8f62;
    --red: #d0202b;
    --white: #ffffff;
    --paper: #ffffff;
    --edge: #b9b9b9;
    --grey-text: #4a4f55;
  }
  * { margin: 0; padding: 0; box-sizing: border-box; }
  html, body { width: 1200px; height: 1000px; overflow: hidden; background: var(--paper); }

  .banner {
    position: absolute;
    left: 445px; top: 77px;
    width: 310px; height: 845px;
    background: var(--white);
    border: 1px solid var(--edge);
    overflow: hidden;
    transform: scale(1.1);
    transform-origin: center;
  }

  .banner__header {
    position: absolute; left: 0; top: 0;
    width: 100%; height: 235px;
    background: linear-gradient(to bottom, var(--green-deep) 0 60%, var(--white) 60% 72%, var(--green-band) 72% 100%);
  }
  .banner__slogan {
    position: absolute; top: 28px; width: 100%;
    text-align: center;
    font-family: "Comfortaa", sans-serif; font-weight: 600;
    color: var(--white); font-size: 27px; line-height: 27px;
    letter-spacing: 0.5px;
  }

  .crest {
    position: absolute; left: 108px; top: 114px;
    width: 94px; height: 94px; border-radius: 50%;
    background: var(--white);
    display: flex; align-items: center; justify-content: center;
    text-align: center;
    font-family: "Poppins", sans-serif; font-weight: 600;
    font-size: 12px; line-height: 14px; color: var(--green-deep);
  }

  .cheer {
    position: absolute; left: 6px; top: 226px;
    width: 298px; height: 120px;
  }
  .cheer svg { position: absolute; inset: 0; }
  .cheer__text {
    position: absolute; inset: 0;
    display: flex; flex-direction: column; align-items: center; justify-content: center;
    font-family: "Open Sans", sans-serif; color: var(--red);
    font-size: 20.5px; line-height: 24px; text-align: center;
    transform: rotate(5deg);
  }

  .fan-photo {
    position: absolute; left: 30px; top: 355px;
    width: 250px; height: 268px;
    background: radial-gradient(ellipse at 50% 45%, #d8d2c4 0%, #b4bcc4 45%, #ffffff 80%);
  }

  .sponsor-band {
    position: absolute; left: 0; top: 632px;
    width: 100%; height: 104px;
    background: var(--green-band);
  }
  .sponsor {
    position: absolute; left: 115px; top: 633px;
    width: 110px; height: 78px;
    background: var(--white); border-radius: 5px;
    display: flex; flex-direction: column; align-items: center; justify-content: center; gap: 8px;
    font-family: "Poppins", sans-serif; font-weight: 600;
    font-size: 13px; color: var(--grey-text); letter-spacing: 1px;
  }
  .sponsor__mark { width: 26px; height: 26px; background: var(--grey-text); }

  .social {
    position: absolute; left: 0; top: 736px;
    width: 100%; height: 109px;
    background: var(--white);
  }
  .social__brand {
    position: absolute; left: 12px; top: 14px;
    width: 68px;
    display: flex; flex-direction: column; align-items: center; gap: 4px;
    font-family: "Poppins", sans-serif; font-weight: 600;
    font-size: 11px; color: var(--green-text);
  }
  .social__square { width: 50px; height: 50px; border-radius: 8px; background: var(--green-text); }
  .social__handles {
    position: absolute; left: 92px; top: 6px;
    list-style: none;
    font-family: "Poppins", sans-serif; font-weight: 600;
    font-size: 12.5px; line-height: 19px; color: var(--green-text);
  }
</style>
</head>
<body>
  <main class="banner">
    <header class="banner__header">
      <p class="banner__slogan">CONTIGO<br>SIEMPRE</p>
    </header>

    <div class="crest">Liga<br>Tricolor</div>

    <section class="cheer">
      <svg viewBox="0 0 298 120" width="298" height="120" aria-hidden="true">
        <path d="M4 20 C 70 2, 130 8, 180 18 C 225 27, 265 30, 294 22 L 294 112 C 250 118, 215 110, 170 100 C 110 88, 60 86, 4 94 Z"
              fill="#ffffff" stroke="#1f6b45" stroke-width="2"/>
      </svg>
      <div class="cheer__text">
        <span>'Vamos México,</span>
        <span>vamos Selección!</span>
        <span>Contigo siempre de corazón!</span>
      </div>
    </section>

    <div class="fan-photo" role="img" aria-label="Photo of a jumping fan in a Mexico jersey and jeans, arms and legs spread, holding up the cheer banner"></div>

    <section class="sponsor-band"></section>
    <div class="sponsor">
      <span class="sponsor__mark"></span>
      <span>ONDALIRA</span>
    </div>

    <footer class="social">
      <div class="social__brand">
        <span class="social__square"></span>
        <span>fotelia</span>
      </div>
      <ul class="social__handles">
        <li>@ravitelbor81 @quorvent907</li>
        <li>#nublandoyo</li>
        <li>#tiapasaloscaramelos</li>
        <li>#guardianesdelmaizdorado</li>
        <li>#verbena2031</li>
      </ul>
    </footer>
  </main>
</body>
</html>
```